Powerpoint Template needed for new Digital Consultancy

We have recently had our logo designed through Brushvale and would now like to extend the brand look & feel through to having a powerpoint template created that we can use as a master template within which to create our client presentations.
Typical slides required and in terms of what we would need templating is:

- Stylised header and footer for main content slides
- intro/front page slide
- contents page slide
- standardised font type and sizes, heading types (including sizes) for Level 1, Level 2 and Level 3 headings
- use of text colour and any standards/styling around when to use bold, underline, italics etc
- table styling for when we want to use tables in the presentation
- standards and styles around using bullet and number lists
- stylising use of imagery that is dropped in e.g. do all images have a certain border style or drop-shadow etc.
- style and slide layout/format for how team profiles are handled
- style and slide layout/format for how case studies are handled
- closing, contact-us page

We can send over logo files and colour/font styles etc used for the logo soon.

Target Market(s)

B2B professional clients that are either medium to large corporations or potentially some government departments.

Industry/Entity Type

Digital

Font styles to use
Sans Serif

Colors
ec1f27
f37122
f78f20
faa54b
f68d4d
0255a3

Requirements
Must have
• Ideally as many templated pages/master slide types as outlined above in the brief to meet the requirements of what the powerpoint deck will be used for. Namely client presentations and pitches.
• Versions of the logo are attached to give an idea of the colour palette and clean, modern style we are looking for, plus the type of font we are using and like.
• We are looking for the slide design to be modern, minimalistic, clean and not overuse of colour. Preferably a white slide background so it's easy to then read slide content when we populate the slides with text which will be in black.
Nice to have
• Not expecting to see too much more than simple use of the logo and a slide header perhaps using some sort of line as a break and then a simple footer as well.
• Consider using Abode font.
Should not have
• Too much block colour or elements that draw away from what will go in the main content body of our slides when we use them.

```html
<!DOCTYPE html>
<html lang="en">
<head>
<meta charset="utf-8">
<title>Orbitline Presentation Template</title>
<link href="https://fonts.googleapis.com/css2?family=Exo+2:wght@300;400;500&family=Open+Sans:ital,wght@0,400;0,700;1,400&display=swap" rel="stylesheet">
<style>
:root{
  --red:#ec1f27;
  --orange:#f37122;
  --amber:#f78f20;
  --light-orange:#faa54b;
  --board:#7a4a2c;
  --paper:#ffffff;
  --paper-soft:#f3f3f3;
  --ink:#222222;
  --muted:#8a8a8a;
}
*{box-sizing:border-box;margin:0;padding:0}
html,body{width:1200px;height:1128px;overflow:hidden}
body{background:var(--board);font-family:"Open Sans",sans-serif;color:var(--ink);position:relative}
.slide{position:absolute;width:392px;height:220px;background:var(--paper);overflow:hidden}
.c1{left:8px}.c2{left:404px}.c3{left:800px}
.r1{top:6px}.r2{top:230px}.r3{top:454px}.r4{top:678px}.r5{top:902px}
.abs{position:absolute}
.photo{position:absolute}

.brand{position:absolute;font-family:"Exo 2",sans-serif;font-weight:500;color:var(--red);white-space:nowrap;line-height:1}

.hdr{position:absolute;left:0;top:0;width:392px;height:38px}
.title{position:absolute;left:12px;top:12px;font-family:"Exo 2",sans-serif;font-weight:300;font-size:15px;color:#fff;letter-spacing:.2px}
.hdr-brand{right:10px;top:13px;font-size:9px}

.url-tab{position:absolute;left:0;bottom:10px;height:7px;width:96px;background:var(--red);color:#fff;font-size:4.5px;line-height:7px;padding-left:11px}
.copy{position:absolute;left:0;right:0;bottom:4px;text-align:center;font-size:4.5px;color:var(--muted)}
.page{position:absolute;right:12px;bottom:5px;width:16px;height:11px;background:var(--orange);color:#fff;font-size:6px;line-height:11px;text-align:center}

.body{font-size:4.6px;line-height:1.45;color:#333}
.body p{margin-bottom:4px}
.hl{color:var(--red)}

.toc-item{position:absolute;display:flex;align-items:center;gap:12px;font-size:8px;color:#444}
.toc-num{width:30px;height:20px;background:var(--red);color:#fff;font-size:10px;text-align:center;line-height:20px;font-family:"Exo 2",sans-serif}

.member{position:absolute;top:46px;width:86px;text-align:center}
.member .face{width:44px;height:44px;margin:0 auto;background:linear-gradient(#b7b7b7,#6f6f6f)}
.member .name{font-family:"Exo 2",sans-serif;font-size:10px;color:var(--red);margin-top:9px;line-height:1}
.member .role{font-size:6px;color:var(--light-orange);line-height:1.2}
.member .bio{font-size:4.6px;line-height:1.4;color:#333;margin-top:8px;padding:0 4px}

.feature{position:absolute;width:86px;text-align:center}
.feature svg{width:26px;height:26px;display:block;margin:0 auto}
.feature .lbl{font-size:5.6px;font-weight:700;color:var(--red);margin-top:4px}
.feature .desc{font-size:4.4px;line-height:1.4;color:#aaa;margin-top:2px}

.grid{position:absolute;left:52px;top:64px;width:290px;border-collapse:collapse;font-size:5px;text-align:center}
.grid th{background:var(--red);color:#fff;font-weight:400;height:12px;border-right:1px solid #fff}
.grid td{height:14.7px;border-right:1px solid #fff;border-bottom:1px solid #fff;background:#e6e8ee}
.grid tr:nth-child(even) td{background:#d4d8e2}
.grid td.ph{background:var(--red);color:#fff}
.grid tr:nth-child(even) td.ph{background:#f04a4f}

.badge{position:absolute;width:80px;text-align:center;color:#fff}
.badge .dot{width:44px;height:44px;margin:0 auto;border-radius:50%;background:#fff;border:3px solid var(--red);box-shadow:0 0 0 2px #fff;display:flex;align-items:center;justify-content:center}
.badge .dot svg{width:22px;height:22px}
.badge .lbl{font-size:5.8px;font-weight:700;margin-top:6px}
.badge .desc{font-size:4.6px;line-height:1.35}
</style>
</head>
<body>

<section class="slide c1 r1">
  <div class="photo" style="inset:0;background:linear-gradient(180deg,#e4e4e4 0%,#cfcfcf 55%,#a9a9a9 100%)" role="img" aria-label="Boardroom with conference table and black chairs, presentation screen on the wall"></div>
  <div class="abs" style="left:88px;top:14px;width:240px;height:94px;background:#f7f7f7;box-shadow:0 1px 3px rgba(0,0,0,.2)"></div>
  <div class="brand" style="left:116px;top:34px;font-size:20px">orbitline</div>
  <div class="abs" style="left:117px;top:72px;font-family:'Exo 2',sans-serif;font-weight:300;font-size:16px;color:var(--red)">PRESENTATION TITLE</div>
  <div class="abs" style="left:118px;top:92px;font-size:6.5px;color:var(--orange)">Place Title detail or Description here</div>
  <svg class="abs" style="left:0;bottom:0" width="392" height="14" viewBox="0 0 392 14"><polygon points="240,14 392,14 392,2 252,2" fill="var(--red)"/><polygon points="256,14 268,14 256,2 244,2" fill="#fff"/><polygon points="0,14 248,14 236,2 0,2" fill="var(--orange)"/></svg>
  <div class="abs" style="right:14px;bottom:2px;font-size:6px;color:#fff">www.orbitline.com.au</div>
</section>

<section class="slide c2 r1">
  <div class="brand" style="left:10px;top:48px;font-size:20px">orbitline</div>
  <div class="abs" style="left:0;top:72px;width:392px;height:108px;background:var(--red)"></div>
  <div class="abs" style="left:10px;top:92px;font-family:'Exo 2',sans-serif;font-weight:300;font-size:21px;color:#fff">PRESENTATION TITLE</div>
  <div class="abs" style="left:12px;top:117px;font-size:9px;color:#fff;font-weight:300">Place Title detail or Description here</div>
  <div class="abs" style="left:0;top:182px;width:96px;height:8px;background:var(--red);color:#fff;font-size:5px;line-height:8px;padding-left:10px">www.orbitline.com.au</div>
</section>

<section class="slide c3 r1">
  <div class="photo" style="left:0;top:0;width:392px;height:150px;background:linear-gradient(135deg,#7d8794,#3a3f46 60%,#c9ccd0)" role="img" aria-label="Business team in suits meeting around a table"></div>
  <svg class="abs" style="left:0;top:122px" width="392" height="98" viewBox="0 0 392 98"><path d="M0 14 C120 34 260 26 392 0 L392 98 L0 98Z" fill="var(--red)"/><path d="M0 22 C120 42 260 34 392 8 L392 98 L0 98Z" fill="#fff"/></svg>
  <div class="brand" style="left:20px;top:186px;font-size:19px">orbitline</div>
  <div class="abs" style="left:38px;top:210px;font-size:4.6px;color:var(--orange)">www.orbitline.com.au</div>
  <div class="abs" style="left:156px;top:176px;width:1px;height:34px;background:var(--red)"></div>
  <div class="abs" style="left:166px;top:180px;font-family:'Exo 2',sans-serif;font-weight:300;font-size:18px;color:var(--red)">PRESENTATION TITLE</div>
  <div class="abs" style="left:167px;top:200px;font-size:7px;color:var(--light-orange)">Place Title detail or Description here</div>
</section>

<section class="slide c1 r2">
  <svg class="hdr" viewBox="0 0 392 38"><polygon points="0,8 298,8 318,34 0,34" fill="var(--red)"/><polygon points="300,8 312,8 332,34 320,34" fill="var(--orange)"/><rect x="0" y="34" width="392" height="1.5" fill="var(--orange)"/></svg>
  <div class="title">Table of Contents</div>
  <div class="brand hdr-brand">orbitline</div>
  <div class="toc-item" style="left:50px;top:46px"><span class="toc-num">01</span>Introduction</div>
  <div class="toc-item" style="left:50px;top:77px"><span class="toc-num">02</span>About Us</div>
  <div class="toc-item" style="left:50px;top:109px"><span class="toc-num">03</span>Our Team</div>
  <div class="toc-item" style="left:50px;top:140px"><span class="toc-num">04</span>Services</div>
  <div class="toc-item" style="left:50px;top:172px"><span class="toc-num">05</span>Solutions</div>
  <div class="toc-item" style="left:228px;top:46px"><span class="toc-num">06</span>Portfolio</div>
  <div class="toc-item" style="left:228px;top:77px"><span class="toc-num">07</span>Pricing</div>
  <div class="toc-item" style="left:228px;top:109px"><span class="toc-num">08</span>Financial Data</div>
  <div class="toc-item" style="left:228px;top:140px"><span class="toc-num">09</span>Testimonial</div>
  <div class="toc-item" style="left:228px;top:172px"><span class="toc-num">10</span>Contact Us</div>
  <div class="url-tab">www.orbitline.com.au</div>
  <div class="copy">Copyright © 2016 Orbitline, All Rights Reserved.</div>
  <div class="page">1</div>
</section>

<section class="slide c2 r2">
  <svg class="hdr" viewBox="0 0 392 38"><polygon points="0,8 298,8 318,34 0,34" fill="var(--red)"/><polygon points="300,8 312,8 332,34 320,34" fill="var(--orange)"/><rect x="0" y="34" width="392" height="1.5" fill="var(--orange)"/></svg>
  <div class="title">Our Mission</div>
  <div class="brand hdr-brand">orbitline</div>
  <div class="abs" style="left:20px;top:42px;width:352px;text-align:center;font-size:6.6px;font-style:italic;color:var(--red);line-height:1.4">The mission of Orbitline is to inspire growth companies to capture opportunities in billion dollar markets by inventing the future.</div>
  <div class="abs body" style="left:12px;top:66px;width:204px">
    <p>We help you achieve the next level of growth, productivity and profitability. Are you anticipating what's going to happen over the next five years? Are you connected to sources of innovation? More importantly, are your competitors?</p>
    <p>Internet of Things, Big Data and Analytics, 3D Printing, and more ... We have the expertise to help Business Leaders discover what's possible, identify exceptional opportunities, and create value in the New IoT Economy.</p>
    <p><span class="hl">Innovation is not mystical.</span> Innovation is methodical and planned. Innovation is necessary. Getting involved in the startup and VC ecosystem is an important step. We can show you how.</p>
    <p><span class="hl">Innovation is created</span> by strategically connecting marketplace trends with specific project planning. Innovation has developed business-driven innovation for anticipating future realities, identifying innovation, and accessing new revenue.</p>
  </div>
  <div class="photo" style="left:218px;top:74px;width:156px;height:92px;background:linear-gradient(135deg,#dfe6ee,#8b98a6);box-shadow:0 4px 6px rgba(0,0,0,.25)" role="img" aria-label="Business people at office windows with laptop and charts in the foreground"></div>
  <div class="url-tab">www.orbitline.com.au</div>
  <div class="copy">Copyright © 2016 Orbitline, All Rights Reserved.</div>
  <div class="page">1</div>
</section>

<section class="slide c3 r2">
  <svg class="hdr" viewBox="0 0 392 38"><polygon points="0,8 298,8 318,34 0,34" fill="var(--red)"/><polygon points="300,8 312,8 332,34 320,34" fill="var(--orange)"/><rect x="0" y="34" width="392" height="1.5" fill="var(--orange)"/></svg>
  <div class="title">Our Team</div>
  <div class="brand hdr-brand">orbitline</div>
  <div class="member" style="left:13px"><div class="face" role="img" aria-label="Portrait photo of team member"></div><div class="name">John Doe</div><div class="role">Manager</div><div class="bio">Lorem ipsum dolor sit amet consectetur adipiscing elit. Vestibulum nec eros in dolor posuere interdum.<br><br>Lorem ipsum dolor sit amet consectetur adipiscing elit. Vestibulum nec eros in dolor posuere interdum.</div></div>
  <div class="member" style="left:107px"><div class="face" role="img" aria-label="Portrait photo of team member"></div><div class="name">John Doe</div><div class="role">Manager</div><div class="bio">Lorem ipsum dolor sit amet consectetur adipiscing elit. Vestibulum nec eros in dolor posuere interdum.<br><br>Lorem ipsum dolor sit amet consectetur adipiscing elit. Vestibulum nec eros in dolor posuere interdum.</div></div>
  <div class="member" style="left:194px"><div class="face" role="img" aria-label="Portrait photo of team member"></div><div class="name">John Doe</div><div class="role">Manager</div><div class="bio">Lorem ipsum dolor sit amet consectetur adipiscing elit. Vestibulum nec eros in dolor posuere interdum.<br><br>Lorem ipsum dolor sit amet consectetur adipiscing elit. Vestibulum nec eros in dolor posuere interdum.</div></div>
  <div class="member" style="left:281px"><div class="face" role="img" aria-label="Portrait photo of team member"></div><div class="name">John Doe</div><div class="role">Manager</div><div class="bio">Lorem ipsum dolor sit amet consectetur adipiscing elit. Vestibulum nec eros in dolor posuere interdum.<br><br>Lorem ipsum dolor sit amet consectetur adipiscing elit. Vestibulum nec eros in dolor posuere interdum.</div></div>
  <div class="url-tab">www.orbitline.com.au</div>
  <div class="copy">Copyright © 2016 Orbitline, All Rights Reserved.</div>
  <div class="page">1</div>
</section>

<section class="slide c1 r3">
  <svg class="hdr" viewBox="0 0 392 38"><polygon points="0,8 298,8 318,34 0,34" fill="var(--red)"/><polygon points="300,8 312,8 332,34 320,34" fill="var(--orange)"/><rect x="0" y="34" width="392" height="1.5" fill="var(--orange)"/></svg>
  <div class="title">Two Column</div>
  <div class="brand hdr-brand">orbitline</div>
  <div class="abs body" style="left:16px;top:46px;width:170px">
    <p>There are many variations of passages of lorem ipsum available, but the majority have suffered alteration in some form, by injected humour, or randomized words which don't look even slightly believable. If you are going to use a passage of lorem ipsum, you need to be sure there isn't anything embarrassing hidden in the middle of text.</p>
    <p>If you are going to use a passage of Lorem Ipsum, you need to be sure there isn't anything embarrassing hidden in the middle of text. All the Lorem Ipsum generators on the Internet tend to repeat predefined chunks as necessary.</p>
    <p>It uses a dictionary of over 200 Latin words, combined with a handful of model sentence structures, to generate Lorem Ipsum which looks reasonable and free from repetition.</p>
    <p>There are many variations of passages of lorem ipsum available, but the majority have suffered alteration in some form.</p>
  </div>
  <div class="abs body" style="left:206px;top:46px;width:170px">
    <p>There are many variations of passages of lorem ipsum available, but the majority have suffered alteration in some form, by injected humour, or randomized words which don't look even slightly believable. If you are going to use a passage of lorem ipsum, you need to be sure there isn't anything embarrassing hidden in the middle of text.</p>
    <p>If you are going to use a passage of Lorem Ipsum, you need to be sure there isn't anything embarrassing hidden in the middle of text. All the Lorem Ipsum generators on the Internet tend to repeat predefined chunks as necessary.</p>
    <p>It uses a dictionary of over 200 Latin words, combined with a handful of model sentence structures, to generate Lorem Ipsum which looks reasonable and free from repetition.</p>
    <p>There are many variations of passages of lorem ipsum available, but the majority have suffered alteration in some form.</p>
  </div>
  <div class="url-tab">www.orbitline.com.au</div>
  <div class="copy">Copyright © 2016 Orbitline, All Rights Reserved.</div>
  <div class="page">1</div>
</section>

<section class="slide c2 r3">
  <div class="photo" style="left:0;top:30px;width:392px;height:104px;background:linear-gradient(135deg,#5a4636,#a88e75 50%,#3f3128)" role="img" aria-label="Hands writing in a notebook beside a glass of water and a tablet on a wooden desk"></div>
  <svg class="hdr" viewBox="0 0 392 38"><polygon points="0,8 298,8 318,34 0,34" fill="var(--red)"/><polygon points="300,8 312,8 332,34 320,34" fill="var(--orange)"/><rect x="0" y="34" width="392" height="1.5" fill="var(--orange)"/></svg>
  <div class="title">Image</div>
  <div class="brand hdr-brand">orbitline</div>
  <div class="abs" style="left:10px;top:136px;font-size:8px;color:var(--orange)">Heading</div>
  <div class="abs body" style="left:10px;top:147px;width:372px">
    <p>There are many variations of passages of lorem ipsum available, but the majority have suffered alteration in some form, by injected humour, or randomized words which don't look even slightly believable. If you are going to use a passage of lorem ipsum, you need to be sure there isn't anything embarrassing hidden in the middle of text.</p>
    <p>If you are going to use a passage of Lorem Ipsum, you need to be sure there isn't anything embarrassing hidden in the middle of text. All the Lorem Ipsum generators on the Internet tend to repeat predefined chunks as necessary. It uses a dictionary of over 200 Latin words.</p>
  </div>
  <div class="url-tab">www.orbitline.com.au</div>
  <div class="copy">Copyright © 2016 Orbitline, All Rights Reserved.</div>
  <div class="page">1</div>
</section>

<section class="slide c3 r3">
  <svg class="hdr" viewBox="0 0 392 38"><polygon points="0,8 298,8 318,34 0,34" fill="var(--red)"/><polygon points="300,8 312,8 332,34 320,34" fill="var(--orange)"/><rect x="0" y="34" width="392" height="1.5" fill="var(--orange)"/></svg>
  <div class="title">Icons</div>
  <div class="brand hdr-brand">orbitline</div>
  <div class="feature" style="left:20px;top:50px"><svg viewBox="0 0 26 26" fill="none" stroke="var(--red)" stroke-width="2"><rect x="3" y="3" width="10" height="18" rx="1.5"/><rect x="13" y="8" width="10" height="15" rx="1.5"/></svg><div class="lbl">Relationship</div><div class="desc">Nullam eu tempor purus. Nunc a leo magna, consequat risus. Nullam eu.</div></div>
  <div class="feature" style="left:108px;top:50px"><svg viewBox="0 0 26 26" fill="var(--red)"><rect x="3" y="10" width="13" height="13"/><rect x="10" y="3" width="13" height="13" stroke="#fff" stroke-width="1.5"/></svg><div class="lbl">Double Data</div><div class="desc">Nullam eu tempor purus. Nunc a leo magna, consequat risus. Nullam eu.</div></div>
  <div class="feature" style="left:196px;top:50px"><svg viewBox="0 0 26 26" fill="none" stroke="var(--red)" stroke-width="2"><circle cx="13" cy="14" r="9"/><path d="M13 9v5l3 3M4 5l4-3M22 5l-4-3"/></svg><div class="lbl">Time Up</div><div class="desc">Nullam eu tempor purus. Nunc a leo magna, consequat risus. Nullam eu.</div></div>
  <div class="feature" style="left:284px;top:50px"><svg viewBox="0 0 26 26" fill="var(--red)"><polygon points="17,1 6,15 12,15 8,25 20,10 14,10"/></svg><div class="lbl">Fast Response</div><div class="desc">Nullam eu tempor purus. Nunc a leo magna, consequat risus. Nullam eu.</div></div>
  <div class="feature" style="left:20px;top:126px"><svg viewBox="0 0 26 26" fill="none" stroke="var(--red)" stroke-width="3" stroke-linecap="round"><path d="M4 4l18 18M22 4L4 22"/></svg><div class="lbl">Responsive</div><div class="desc">Nullam eu tempor purus. Nunc a leo magna, consequat risus. Nullam eu.</div></div>
  <div class="feature" style="left:108px;top:126px"><svg viewBox="0 0 26 26" fill="none" stroke="var(--red)" stroke-width="2"><path d="M10 2v10M16 2v10"/><circle cx="13" cy="18" r="6"/></svg><div class="lbl">Award</div><div class="desc">Nullam eu tempor purus. Nunc a leo magna, consequat risus. Nullam eu.</div></div>
  <div class="feature" style="left:196px;top:126px"><svg viewBox="0 0 26 26" fill="none" stroke="var(--red)" stroke-width="2"><rect x="5" y="2" width="16" height="22" rx="2"/><path d="M11 21h4"/></svg><div class="lbl">Digitalization</div><div class="desc">Nullam eu tempor purus. Nunc a leo magna, consequat risus. Nullam eu.</div></div>
  <div class="feature" style="left:284px;top:126px"><svg viewBox="0 0 26 26" fill="var(--red)"><rect x="12" y="3" width="2.5" height="21"/><polygon points="4,7 20,7 24,10 20,13 4,13"/></svg><div class="lbl">Mapping</div><div class="desc">Nullam eu tempor purus. Nunc a leo magna, consequat risus. Nullam eu.</div></div>
  <div class="url-tab">www.orbitline.com.au</div>
  <div class="copy">Copyright © 2016 Orbitline, All Rights Reserved.</div>
  <div class="page">1</div>
</section>

<section class="slide c1 r4" style="background:var(--paper-soft)">
  <div class="brand" style="left:14px;top:33px;font-size:12px">orbitline</div>
  <div class="abs" style="left:84px;top:26px;width:1px;height:26px;background:#555"></div>
  <div class="abs" style="left:92px;top:29px;font-family:'Exo 2',sans-serif;font-weight:300;font-size:14px;color:#333">Section Divider</div>
  <div class="abs" style="left:0;top:84px;width:340px;height:54px;background:var(--red)"></div>
  <div class="abs" style="left:340px;top:84px;width:52px;height:54px;background:var(--orange)"></div>
  <svg class="abs" style="left:352px;top:97px" width="28" height="28" viewBox="0 0 28 28" fill="none" stroke="#fff" stroke-width="1.6"><circle cx="14" cy="14" r="12"/><path d="M8 14h12M15 9l5 5-5 5"/></svg>
  <div class="abs" style="left:84px;top:96px;width:180px;font-size:5.2px;line-height:1.5;color:#fde0d8">Lorem ipsum dolor sit amet, consectetur adipiscing elit. Vestibulum nec eros in dolor posuere interdum. Ut elementum, justo vel pretium condimentum, ante metus sodales nisi, eu aliquet.</div>
</section>

<section class="slide c2 r4">
  <svg class="hdr" viewBox="0 0 392 38"><polygon points="0,8 298,8 318,34 0,34" fill="var(--red)"/><polygon points="300,8 312,8 332,34 320,34" fill="var(--orange)"/><rect x="0" y="34" width="392" height="1.5" fill="var(--orange)"/></svg>
  <div class="title">Table</div>
  <div class="brand hdr-brand">orbitline</div>
  <div class="abs" style="left:34px;top:42px;width:330px;font-size:6px;line-height:1.4;color:#333">Lorem ipsum dolor sit amet, consectetur adipiscing elit. Vestibulum nec eros in dolor posuere interdum. Ut elementum, justo vel pretium condimentum,</div>
  <table class="grid">
    <tr><th style="background:#fff"></th><th>JAN</th><th>FEB</th><th>MAR</th><th>APR</th><th>MAY</th><th>JUN</th></tr>
    <tr><td class="ph">Phase1</td><td>XX</td><td>XX</td><td>XX</td><td>XX</td><td>XX</td><td>XX</td></tr>
    <tr><td class="ph">Phase1</td><td>XX</td><td>XX</td><td>XX</td><td>XX</td><td>XX</td><td>XX</td></tr>
    <tr><td class="ph">Phase1</td><td>XX</td><td>XX</td><td>XX</td><td>XX</td><td>XX</td><td>XX</td></tr>
    <tr><td class="ph">Phase1</td><td>XX</td><td>XX</td><td>XX</td><td>XX</td><td>XX</td><td>XX</td></tr>
    <tr><td class="ph">Phase1</td><td>XX</td><td>XX</td><td>XX</td><td>XX</td><td>XX</td><td>XX</td></tr>
    <tr><td class="ph">Phase1</td><td>XX</td><td>XX</td><td>XX</td><td>XX</td><td>XX</td><td>XX</td></tr>
    <tr><td class="ph">Phase1</td><td>XX</td><td>XX</td><td>XX</td><td>XX</td><td>XX</td><td>XX</td></tr>
  </table>
  <div class="abs" style="left:0;right:0;top:184px;text-align:center;font-size:6px;color:#333">Lorem ipsum dolor sit amet, consectetur adipiscing elit. Vestibulum nec eros in dolor posuere interdum</div>
  <div class="url-tab">www.orbitline.com.au</div>
  <div class="copy">Copyright © 2016 Orbitline, All Rights Reserved.</div>
  <div class="page">1</div>
</section>

<section class="slide c3 r4">
  <svg class="hdr" viewBox="0 0 392 38"><polygon points="0,8 298,8 318,34 0,34" fill="var(--red)"/><polygon points="300,8 312,8 332,34 320,34" fill="var(--orange)"/><rect x="0" y="34" width="392" height="1.5" fill="var(--orange)"/></svg>
  <div class="title">Graph</div>
  <div class="brand hdr-brand">orbitline</div>
  <div class="abs" style="left:30px;top:42px;width:340px;font-size:6px;line-height:1.4;color:#333">Lorem ipsum dolor sit amet, consectetur adipiscing elit. Vestibulum nec eros in dolor posuere interdum. Ut elementum, justo vel pretium condimentum,</div>
  <svg class="abs" style="left:0;top:60px" width="392" height="120" viewBox="0 0 392 120" font-family="Open Sans, sans-serif">
    <g font-size="5" fill="#333" text-anchor="end">
      <text x="40" y="104">0</text><text x="40" y="89.6">1</text><text x="40" y="75">2</text><text x="40" y="60.4">3</text><text x="40" y="46">4</text><text x="40" y="31.3">5</text><text x="40" y="16.6">6</text>
    </g>
    <line x1="44" y1="102" x2="370" y2="102" stroke="#bbb" stroke-width=".6"/>
    <g>
      <rect x="58" y="39" width="16" height="63" fill="var(--amber)"/><rect x="74" y="67" width="16" height="35" fill="var(--light-orange)"/><rect x="90" y="73" width="16" height="29" fill="var(--red)"/>
      <rect x="138" y="65" width="16" height="37" fill="var(--light-orange)"/><rect x="154" y="38" width="16" height="64" fill="var(--amber)"/><rect x="170" y="73" width="16" height="29" fill="var(--red)"/>
      <rect x="218" y="51" width="16" height="51" fill="var(--amber)"/><rect x="234" y="76" width="16" height="26" fill="var(--light-orange)"/><rect x="250" y="58" width="16" height="44" fill="var(--red)"/>
      <rect x="296" y="36" width="16" height="66" fill="var(--amber)"/><rect x="312" y="61" width="16" height="41" fill="var(--light-orange)"/><rect x="328" y="29" width="16" height="73" fill="var(--red)"/>
    </g>
    <rect x="208" y="12" width="44" height="20" fill="var(--red)"/><polygon points="226,32 234,32 230,36" fill="var(--red)"/>
    <text x="230" y="26" font-size="10" fill="#fff" text-anchor="middle">87%</text>
    <g font-size="5" fill="var(--red)" text-anchor="middle"><text x="82" y="110">Category 1</text><text x="162" y="110">Category 2</text><text x="242" y="110">Category 3</text><text x="320" y="110">Category 4</text></g>
  </svg>
  <div class="abs" style="left:0;right:0;top:184px;text-align:center;font-size:6px;color:#333">Lorem ipsum dolor sit amet, consectetur adipiscing elit. Vestibulum nec eros in dolor posuere interdum</div>
  <div class="url-tab">www.orbitline.com.au</div>
  <div class="copy">Copyright © 2016 Orbitline, All Rights Reserved.</div>
  <div class="page">1</div>
</section>

<section class="slide c1 r5">
  <div class="photo" style="left:0;top:0;width:392px;height:136px;background:linear-gradient(90deg,#ededed,#d2d2d2 60%,#b9bcc2)" role="img" aria-label="Businessman sketching a business growth diagram on a wall"></div>
  <div class="abs" style="left:0;top:136px;width:392px;height:84px;background:var(--red)"></div>
  <div class="badge" style="left:34px;top:114px"><div class="dot"><svg viewBox="0 0 22 22" fill="none" stroke="var(--red)" stroke-width="2"><circle cx="13" cy="9" r="6"/><path d="M9 13l-6 6"/></svg></div><div class="lbl">Spying</div><div class="desc">Nullam eu tempor purus. Nunc a leo magna, sit amet consequat risus. Nullam eu tempor purus.</div></div>
  <div class="badge" style="left:118px;top:114px"><div class="dot"><svg viewBox="0 0 22 22" fill="none" stroke="var(--red)" stroke-width="2"><rect x="3" y="7" width="15" height="9"/><rect x="5" y="9" width="7" height="5" fill="var(--red)" stroke="none"/><path d="M19 10v3"/></svg></div><div class="lbl">More Power</div><div class="desc">Nullam eu tempor purus. Nunc a leo magna, sit amet consequat risus. Nullam eu tempor purus.</div></div>
  <div class="badge" style="left:206px;top:114px"><div class="dot"><svg viewBox="0 0 22 22" fill="none" stroke="var(--red)" stroke-width="2"><circle cx="11" cy="11" r="8"/><path d="M11 11l4-3"/></svg></div><div class="lbl">Quick</div><div class="desc">Nullam eu tempor purus. Nunc a leo magna, sit amet consequat risus. Nullam eu tempor purus.</div></div>
  <div class="badge" style="left:292px;top:114px"><div class="dot"><svg viewBox="0 0 22 22" fill="var(--red)"><polygon points="11,2 4,19 18,19"/><rect x="2" y="18" width="18" height="2"/></svg></div><div class="lbl">Warning</div><div class="desc">Nullam eu tempor purus. Nunc a leo magna, sit amet consequat risus. Nullam eu tempor purus.</div></div>
</section>

<section class="slide c2 r5">
  <div class="photo" style="left:0;top:0;width:392px;height:160px;background:linear-gradient(135deg,#eeeeea,#dcdcd6)" role="img" aria-label="Street map of the office location with a pin marker"></div>
  <svg class="hdr" viewBox="0 0 392 38"><polygon points="0,8 298,8 318,34 0,34" fill="var(--red)"/><polygon points="300,8 312,8 332,34 320,34" fill="var(--orange)"/><rect x="0" y="34" width="392" height="1.5" fill="var(--orange)"/></svg>
  <div class="title">Contact us</div>
  <div class="brand hdr-brand">orbitline</div>
  <svg class="abs" style="left:184px;top:52px" width="8" height="11" viewBox="0 0 8 11"><path d="M4 11C1 7 0 5 0 4a4 4 0 018 0c0 1-1 3-4 7z" fill="var(--red)"/><circle cx="4" cy="4" r="1.4" fill="#fff"/></svg>
  <div class="abs" style="left:0;top:156px;width:392px;height:64px;background:var(--red)"></div>
  <div class="badge" style="left:3px;top:142px;width:100px"><div class="dot" style="width:30px;height:30px;border-width:2px"><svg viewBox="0 0 22 22" style="width:14px;height:14px"><path d="M11 21C5 13 3 10 3 8a8 8 0 0116 0c0 2-2 5-8 13z" fill="var(--red)"/><circle cx="11" cy="8" r="3" fill="#fff"/></svg></div></div>
  <div class="badge" style="left:104px;top:142px;width:100px"><div class="dot" style="width:30px;height:30px;border-width:2px"><svg viewBox="0 0 22 22" style="width:14px;height:14px"><path d="M5 2l4 4-2 3c1 3 3 5 6 6l3-2 4 4-3 3C9 20 2 13 2 5z" fill="var(--red)"/></svg></div></div>
  <div class="badge" style="left:204px;top:142px;width:100px"><div class="dot" style="width:30px;height:30px;border-width:2px"><svg viewBox="0 0 22 22" style="width:14px;height:14px" fill="none" stroke="var(--red)" stroke-width="2"><rect x="2" y="5" width="18" height="12"/><path d="M2 5l9 7 9-7"/></svg></div></div>
  <div class="badge" style="left:296px;top:142px;width:100px"><div class="dot" style="width:30px;height:30px;border-width:2px"><svg viewBox="0 0 22 22" style="width:14px;height:14px" fill="none" stroke="var(--red)" stroke-width="1.8"><circle cx="11" cy="11" r="9"/><ellipse cx="11" cy="11" rx="4" ry="9"/><path d="M2 11h18"/></svg></div></div>
  <div class="abs" style="left:10px;top:186px;font-size:5.8px;font-style:italic;color:#fff;line-height:1.4">Level Three, 48 Harbour Lane<br>Northbay, NSW 2000</div>
  <div class="abs" style="left:120px;top:186px;font-size:5.8px;font-style:italic;color:#fff">+61 (0) 400 000 123</div>
  <div class="abs" style="left:210px;top:186px;font-size:5.8px;font-style:italic;color:#fff">hello@orbitline.com.au</div>
  <div class="abs" style="left:306px;top:186px;font-size:5.8px;font-style:italic;color:#fff">www.orbitline.com.au</div>
</section>

<section class="slide c3 r5">
  <div class="brand" style="left:10px;top:30px;font-size:20px">orbitline</div>
  <div class="photo" style="left:0;top:70px;width:392px;height:136px;background:linear-gradient(135deg,#2d4763,#6a87a5 55%,#223446)" role="img" aria-label="Close-up of two business people shaking hands"></div>
  <div class="abs" style="left:86px;top:70px;width:180px;height:42px;background:var(--red)"></div>
  <div class="abs" style="left:122px;top:76px;font-size:7px;color:#fff">Thank You for Listening!</div>
  <div class="abs" style="left:122px;top:84px;font-family:'Exo 2',sans-serif;font-weight:300;font-size:18px;color:#fff">QUESTIONS?</div>
  <svg class="abs" style="left:0;bottom:0" width="392" height="14" viewBox="0 0 392 14"><polygon points="252,14 392,14 392,2 264,2" fill="var(--red)"/><polygon points="238,14 250,14 262,2 250,2" fill="var(--orange)"/><polygon points="0,14 236,14 248,2 0,2" fill="#fff"/></svg>
  <div class="abs" style="right:14px;bottom:2px;font-size:6px;color:#fff">www.orbitline.com.au</div>
</section>

</body>
</html>
```